Home Page Improvement for Web Application

Need drastic home page improvement. Currently it looks very amateur.
Basic navigation text elements position must remain due to CSS (See attached template). However, everything else must be redesigned. Fonts,size, typeface, styles, color, layers, backgrounds, images, buttons, logo typeface, etc. Needs to look fresh, original, sleek, balanced, beautiful and professional.
Target Market(s)
Corporate to small business clients
Professional Instructional Designers
Industry/Entity Type
It Professional
Requirements
Must have
- IMPORTANT! The is a web application and not a website.
Take a look at Plumtide and Post Badger as good designs of web applications.
http://www.pixelharborhub.com/2010/02/showcase-of-great-web-app-interfaces/
Good example of keeping the colors simple:
http://vell.com/
Nice to have
- Some white space.
Min use of new font styles: http://www.brightquillreview.com/2009/08/07/beautiful-new-free-fonts-for-your-designs/
Use of creative navigation styles:
http://www.brightquillreview.com/2010/01/04/showcase-of-modern-navigation-design-trends/
Should not have
- Generic clipart or icons.
Not too dark.
Mismatched fonts.
clashing color schemes.
The same mock style as the attached template.

```html
<!DOCTYPE html>
<html lang="en">
<head>
<meta charset="utf-8">
<title>CourseForge – Home</title>
<link href="https://fonts.googleapis.com/css2?family=Ubuntu:ital,wght@0,400;0,500;0,700;1,400&family=Kalam:wght@400&display=swap" rel="stylesheet">
<style>
:root{
  --blue:#0a86bf;
  --blue-dark:#06679a;
  --link:#1a8ac4;
  --orange:#f6a510;
  --orange-light:#fbc12a;
  --ink:#333;
  --muted:#888;
  --page:#f5f5f5;
  --line:#dcdcdc;
  --panel:#ffffff;
  --grey-tab:#c8c8c8;
}
*{box-sizing:border-box;margin:0;padding:0}
html,body{width:1200px;height:1075px;overflow:hidden}
body{background:var(--page);font-family:'Ubuntu',sans-serif;color:var(--ink);position:relative}
a{color:var(--link);text-decoration:none}
.abs{position:absolute}
.topbar{left:0;top:0;width:1200px;height:3px;background:#3a3a3a}

.btn-top{top:3px;height:24px;width:114px;border-radius:0 0 3px 3px;color:#fff;font-size:14px;font-weight:500;display:flex;align-items:center;justify-content:center}
.btn-post-project{left:778px;background:linear-gradient(#1599d4,var(--blue-dark))}
.btn-invite{left:896px;background:linear-gradient(var(--orange-light),var(--orange))}

.brand{left:188px;top:20px;display:flex;align-items:center;gap:8px}
.brand-name{font-size:38px;font-weight:500;color:var(--blue);letter-spacing:-0.5px}
.brand-square{width:14px;height:14px;background:var(--orange)}
.tagline{left:189px;top:62px;font-size:12px;font-style:italic;color:#999;letter-spacing:0.3px}
.welcome{right:190px;top:56px;font-size:12px;color:#444}

.main-nav{left:189px;top:94px;width:823px;height:43px;border-radius:3px;background:linear-gradient(#1ba3dc,#0a7fb6 55%,#0670a4);box-shadow:0 0 0 1px #a9d5ea}
.main-nav a{position:absolute;top:0;line-height:43px;color:#fff;font-size:17px;font-weight:500;transform:translateX(-50%);text-shadow:0 1px 1px rgba(0,0,0,.3)}

.hero{left:189px;top:162px;width:823px;height:311px;background:var(--panel);border:1px solid var(--line);border-radius:4px;overflow:hidden}
.hero-stage{left:0;top:0;width:652px;height:256px;background:linear-gradient(160deg,#f2f2f2,#dedede)}
.hero-side-top{left:652px;top:0;width:171px;height:129px;background:linear-gradient(#d6d6d6,#bdbdbd);color:#fff;font-size:22px;font-weight:500;text-align:center;display:flex;align-items:center;justify-content:center;line-height:1.15}
.hero-side-bottom{left:652px;top:129px;width:171px;height:127px;background:linear-gradient(var(--orange-light),var(--orange));color:#fff;font-size:22px;font-weight:500;text-align:center;display:flex;align-items:center;justify-content:center;line-height:1.15}
.hero-pointer{left:643px;top:46px}

.tab{height:33px;background:linear-gradient(#e2e2e2,#c6c6c6);border:1px solid #bbb;color:#fff;font-size:16px;font-weight:500;display:flex;align-items:center;justify-content:center;text-shadow:0 1px 1px rgba(0,0,0,.25)}
.tab-fold{width:0;height:0;border-left:9px solid transparent;border-bottom:9px solid #a9a9a9}

.steps{left:210px;top:202px;font-family:'Kalam',cursive;font-size:25px;color:var(--blue);line-height:43px}
.steps-underline{left:343px;top:322px}
.illustration{left:527px;top:171px;width:279px;height:168px;border-radius:6px;background:radial-gradient(ellipse at center,#ececec,#dcdcdc)}
.caption{left:560px;top:350px;width:244px;text-align:center;font-family:'Kalam',cursive;font-size:23px;color:var(--blue);line-height:26px}

.project-label{left:200px;top:435px;font-size:15px;color:var(--muted)}
.project-input{left:308px;top:427px;width:560px;height:40px;border:1px solid #d0d0d0;border-radius:5px;background:#fff;box-shadow:inset 0 1px 2px rgba(0,0,0,.06)}
.btn-post{left:882px;top:427px;width:123px;height:40px;border-radius:5px;background:linear-gradient(#1ba3dc,#0670a4);color:#fff;font-size:22px;font-weight:500;display:flex;align-items:center;justify-content:center}

.stats{left:189px;top:500px;width:823px;height:35px;background:#fff;border:1px solid var(--line);border-radius:4px;display:flex;justify-content:space-around;align-items:center;font-size:12.5px;padding:0 14px}
.stats span b{font-weight:400;color:var(--link)}

.showcase{left:189px;top:567px;width:823px;height:231px;background:linear-gradient(#fff,#f1f1f1);border:1px solid var(--line);border-radius:4px}
.thumb{top:611px;width:171px;height:116px;border:3px solid #d2d2d2;background:linear-gradient(#bfe3ef 0%,#e7f1c8 45%,#9cc06a 100%)}
.thumb-meta{top:737px;font-size:11px;line-height:15.5px;color:#333}

.footer-rule{left:188px;width:823px;height:3px;background:#dedede}
.footer-col{top:845px}
.footer-col h3{font-size:19px;font-weight:500;color:#444;margin-bottom:6px}
.footer-col a{display:block;font-size:11px;line-height:17px}
.social{display:flex;gap:7px;margin-top:4px}
.social span{width:27px;height:27px;border-radius:3px}
.s1{background:#3b5b9a}.s2{background:#4fb6e3}.s3{background:#1b7bb4}.s4{background:#f08a1c}
.legal{top:1009px;font-size:11px;color:var(--muted)}
.legal a{font-weight:500}
</style>
</head>
<body>
<div class="abs topbar"></div>

<a class="abs btn-top btn-post-project" href="#">Post a Project</a>
<a class="abs btn-top btn-invite" href="#">Designer Invite</a>

<div class="abs brand"><span class="brand-name">CourseForge</span><span class="brand-square"></span></div>
<div class="abs tagline">Professional Instructional Design &amp; Development</div>
<div class="abs welcome">Welcome, John Smith.</div>

<nav class="abs main-nav">
  <a href="#" style="left:104px">Home</a>
  <a href="#" style="left:300px">Projects</a>
  <a href="#" style="left:505px">Designers</a>
  <a href="#" style="left:715px">Templates</a>
</nav>

<section class="abs hero">
  <div class="abs hero-stage"></div>
  <div class="abs hero-side-top">eLearning<br>Projects</div>
  <div class="abs hero-side-bottom">Instructional<br>Designers</div>
  <svg class="abs hero-pointer" width="10" height="48" viewBox="0 0 10 48"><polygon points="10,0 0,24 10,48" fill="#cfcfcf"/></svg>
</section>
<div class="abs tab-fold" style="left:200px;top:153px"></div>
<div class="abs tab" style="left:209px;top:153px;width:151px">How It Works</div>

<div class="abs steps">1) Post your project.<br>2) Determine your budget.<br>3) Select the best design.</div>
<svg class="abs steps-underline" width="144" height="14" viewBox="0 0 144 14"><path d="M2 12 Q70 0 142 5" stroke="#d44" stroke-width="2" fill="none"/></svg>
<div class="abs illustration" role="img" aria-label="Sketch of several instructional designers each submitting a design board, one circled as the chosen entry"></div>
<div class="abs caption">Instructional designers<br>submit designs</div>

<div class="abs project-label">Project Name:</div>
<div class="abs project-input"></div>
<a class="abs btn-post" href="#">Post</a>

<div class="abs stats">
  <span>Open Projects <b>(100)</b></span>
  <span>Designers available <b>(30)</b></span>
  <span>Projects in progress <b>(300)</b></span>
  <span>Projects Completed <b>(1000)</b></span>
  <span>Templates <b>(2000)</b></span>
</div>

<section class="abs showcase"></section>
<div class="abs tab-fold" style="left:200px;top:556px"></div>
<div class="abs tab" style="left:209px;top:556px;width:187px">Designer Showcase</div>

<div class="abs thumb" style="left:205px" role="img" aria-label="Course screen preview with a school bus and learners on a green hill"></div>
<div class="abs thumb" style="left:411px" role="img" aria-label="Course screen preview with a school bus and learners on a green hill"></div>
<div class="abs thumb" style="left:616px" role="img" aria-label="Course screen preview with a school bus and learners on a green hill"></div>
<div class="abs thumb" style="left:822px" role="img" aria-label="Course screen preview with a school bus and learners on a green hill"></div>

<div class="abs thumb-meta" style="left:205px">Designer: <a href="#">John Doe</a><br>Project Name: <a href="#">Sales WBT</a><br>Authoring Tool: <a href="#">SlideCraft 4.0</a></div>
<div class="abs thumb-meta" style="left:411px">Designer: <a href="#">John Doe</a><br>Project Name: <a href="#">Sales WBT</a><br>Authoring Tool: <a href="#">SlideCraft 4.0</a></div>
<div class="abs thumb-meta" style="left:616px">Designer: <a href="#">John Doe</a><br>Project Name: <a href="#">Sales WBT</a><br>Authoring Tool: <a href="#">SlideCraft 4.0</a></div>
<div class="abs thumb-meta" style="left:822px">Designer: <a href="#">John Doe</a><br>Project Name: <a href="#">Sales WBT</a><br>Authoring Tool: <a href="#">SlideCraft 4.0</a></div>

<div class="abs footer-rule" style="top:824px"></div>

<div class="abs footer-col" style="left:188px">
  <h3>How To</h3>
  <a href="#">Managing a project</a><a href="#">Awarding your project</a><a href="#">Final Changes</a><a href="#">Entering a Project</a><a href="#">What if you win</a>
</div>
<div class="abs footer-col" style="left:393px">
  <h3>Knowledge Base</h3>
  <a href="#">FAQ General</a><a href="#">FAQ Projects</a><a href="#">FAQ Designers</a><a href="#">Announcements</a><a href="#">Tips &amp; Tricks</a><a href="#">Feature Requests</a>
</div>
<div class="abs footer-col" style="left:599px">
  <h3>Customer Service</h3>
  <a href="#">Support</a><a href="#">Submit a request</a><a href="#">Check your existing requests</a>
</div>
<div class="abs footer-col" style="left:805px">
  <h3>Stay in touch</h3>
  <div class="social"><span class="s1"></span><span class="s2"></span><span class="s3"></span><span class="s4"></span></div>
</div>

<div class="abs footer-rule" style="top:995px"></div>
<div class="abs legal" style="left:188px">© 2011 - <a href="#">courseforge.com</a> | All rights reserved.</div>
<div class="abs legal" style="right:189px">Use of this service and this website constitutes acceptence of our <a href="#">terms</a>.</div>
</body>
</html>
```